NURSING: STEP BEYOND THE HEDGEROW

Size of the book cover: 140 x 215 mms

I need a cover for the 30,000 word book I have just written. It is a positive take on what I think nursing is and what it needs to be in the future. It is also my story of being nursed and of being a nurse.

My dream is that nurses honor themselves; that they look to the future with confidence and intelligence and that care continues to be delivered with compassionate person centeredness.

I define nursing as a professional workforce which, with probity, prevent or relieve distress; provide compassionate, safe, excellent care; and which contributes to the organization of healthcare.

The name comes from a Biblical parable Mathew 5:14-16. If a light is hidden under a bushel (basket) it is barely seen. If it is lit out from the basket it is clearly seen. As nurses we must continue to take up our mantel and ensure our light is seen and that it continues to shine the way we want it to.

As nurses we each take up our own lantern of caring, each in our own ways. To walk more brightly in our own paths of service.

The final design should show the specialness of nursing.

Target Market(s)

Nurses present, past and future

Industry/Entity Type

Healthcare

Font styles to use
Sans Serif
Other font styles liked:
• Whatever you think will suit

Colors
ec1f27
0393ce
9bcb3c

Requirements
Must have
• Be friendly, calming.
• NB: I am not sure whether the title should be in uppercase or not. Nursing could be uppercase and step beyond the hedgerow could be lower case. I leave it to you experienced people
Nice to have
• Something that depicts nursing...or is suggestive of nursing and the specialness of the work we do. How we bring our light to our patients as we 'hold them in the palms of out hands' and care for them. How they honor us by allowing us into their lives. Our rich past and out history allows us to be who we are today and we look to the future with confidence and hope
• I like rich colors, eg the color type you might find on a stained glass window in a church - rich emerald green or rich crimson red or the deep blue of a nurses cape
Should not have
• A dark cover
• clutter
• Religious overtone
• I have chosen three colors but they are not in the shading I would like - see above

```html
<!DOCTYPE html>
<html lang="en">
<head>
<meta charset="utf-8">
<title>Nursing: Step Beyond the Hedgerow — Book Cover</title>
<link rel="stylesheet" href="https://fonts.googleapis.com/css2?family=Cinzel:wght@500&family=EB+Garamond:ital,wght@0,400;0,500;1,400&display=swap">
<style>
  :root {
    --page-bg: #ece9e3;
    --navy: #2d3a84;
    --ink-blue: #34406e;
    --amber: #e08a3a;
    --amber-deep: #d27a2c;
    --aqua-wash: #cfe9e2;
    --mint-wash: #e3f1e4;
    --cream-wash: #f8f0d6;
    --butter-wash: #f6df9a;
    --gold-wash: #f1c95f;
    --band: #fbf8ef;
  }
  html, body {
    margin: 0;
    padding: 0;
    width: 1200px;
    height: 849px;
    overflow: hidden;
    background: var(--page-bg);
  }
  .canvas {
    position: relative;
    width: 1200px;
    height: 849px;
  }
  .book-cover {
    position: absolute;
    left: 353px;
    top: 44px;
    width: 494px;
    height: 760px;
    overflow: hidden;
    box-shadow: 0 10px 30px rgba(60, 50, 30, 0.18);
    background:
      radial-gradient(ellipse 60% 30% at 80% 10%, rgba(255,255,255,0.45), transparent 70%),
      radial-gradient(ellipse 70% 25% at 25% 20%, var(--mint-wash), transparent 75%),
      linear-gradient(180deg,
        var(--aqua-wash) 0%,
        var(--mint-wash) 22%,
        var(--cream-wash) 40%,
        var(--butter-wash) 60%,
        var(--gold-wash) 85%,
        var(--butter-wash) 100%);
  }
  .lower-wash {
    position: absolute;
    left: 0; right: 0;
    top: 48%;
    bottom: 0;
    background:
      radial-gradient(ellipse 50% 20% at 30% 30%, rgba(255,240,190,0.6), transparent 70%),
      radial-gradient(ellipse 60% 25% at 75% 75%, rgba(236,184,70,0.45), transparent 70%);
  }
  .author-name {
    position: absolute;
    top: 34px;
    right: 44px;
    margin: 0;
    font: 500 21px "EB Garamond", serif;
    color: var(--ink-blue);
    letter-spacing: 0.3px;
  }
  .hands-illustration {
    position: absolute;
    top: 60px;
    left: 190px;
    width: 270px;
    height: 190px;
    border-radius: 40% 45% 40% 50%;
    background: radial-gradient(ellipse at 50% 55%, rgba(240,190,140,0.55), rgba(240,200,160,0.15) 70%, transparent 80%);
  }
  .title-band {
    position: absolute;
    left: 0; right: 0;
    top: 215px;
    height: 150px;
    background: var(--band);
    opacity: 0.92;
  }
  .title-main {
    position: absolute;
    left: 0; right: 0;
    top: 228px;
    margin: 0;
    text-align: center;
    font: 500 92px "Cinzel", serif;
    color: var(--navy);
    letter-spacing: 4px;
    line-height: 1;
  }
  .title-sub {
    position: absolute;
    left: 0; right: 0;
    top: 330px;
    margin: 0;
    text-align: center;
    font: 500 21px "Cinzel", serif;
    color: var(--amber-deep);
    letter-spacing: 1.5px;
  }
  .cover-quote {
    position: absolute;
    left: 34px;
    right: 34px;
    top: 418px;
    margin: 0;
    font: italic 400 21px/1.3 "EB Garamond", serif;
    color: var(--amber);
  }
  .foreword-credit {
    position: absolute;
    right: 60px;
    top: 538px;
    margin: 0;
    font: 400 13px "EB Garamond", serif;
    color: var(--amber-deep);
    letter-spacing: 0.3px;
  }
</style>
</head>
<body>
<main class="canvas">
  <section class="book-cover" aria-label="Book cover">
    <div class="lower-wash"></div>
    <p class="author-name">Moira Kettering</p>
    <div class="hands-illustration" role="img" aria-label="Line drawing of two hands gently holding each other"></div>
    <div class="title-band"></div>
    <h1 class="title-main">NURSING</h1>
    <p class="title-sub">STEP BEYOND THE HEDGEROW</p>
    <p class="cover-quote">“We each take up our own lantern of caring<br>each in our own ways,<br>to walk more brightly in our own path of<br>service”</p>
    <p class="foreword-credit">Forward by Ruth Halloway RN</p>
  </section>
</main>
</body>
</html>
```